Brightwell Careers Homepage Redesign

Redevelopment work is underway on the Brightwell Careers website www.brightwell-careers.com - one task is to create a more compelling vertically stacked, mobile friendly homepage. The developers are not graphic designers and have been unable to produce an effective enough design. Their latest iteration can be seen @ http://novaquill.co.uk/brightwell_careers/index_5.html

The goal of the current design job is to:

a) produce a homepage design - reworking the attached draft concepts/designs to produce an effective landing page that will entice visitors to respond to the key call to action - to book a meeting with me to discuss their needs
b) ensure the design is aesthetically/functionally aligned with the rest of the site
c) ensure the design supports responsive implementation for viewing on a full range of desktop browsers and mobile devices.

Final output should be in a .psd file with all layers unmerged.

Further details on uploaded docs.

```html
<!DOCTYPE html>
<html lang="en">
<head>
<meta charset="utf-8">
<title>Brightwell Careers – Virtual Leadership Coaching &amp; Assessment</title>
<link href="https://fonts.googleapis.com/css2?family=Ubuntu:wght@300;400;500;700&family=Open+Sans:wght@400;600;700&display=swap" rel="stylesheet">
<style>
:root{
  --brand-blue:#1d5a9e;
  --brand-blue-dark:#153f73;
  --navy:#16335c;
  --navy-deep:#0f2748;
  --orange:#ee7a22;
  --orange-soft:#f39a55;
  --peach:#fbe3cf;
  --sun:#f7c97d;
  --grey-light:#e3e3e3;
  --grey-mid:#dadada;
  --charcoal:#3a3a3a;
  --footer:#333333;
  --text:#444444;
  --white:#ffffff;
}
*{box-sizing:border-box;margin:0;padding:0}
html,body{width:1200px;height:2946px;overflow:hidden}
body{font-family:"Open Sans",Arial,sans-serif;color:var(--text);background:var(--white);position:relative}
section,header,footer{position:absolute;left:0;width:1200px}
.abs{position:absolute}
.ph{position:absolute}
.chev{position:absolute;left:50%;transform:translateX(-50%);width:0;height:0;border-left:30px solid transparent;border-right:30px solid transparent;border-top:18px solid;z-index:3}

/* header */
.site-header{top:0;height:122px;background:var(--white);border-bottom:4px solid var(--brand-blue)}
.brand{left:134px;top:26px;display:flex;align-items:center;gap:12px}
.brand-mark{width:44px;height:44px;border-radius:50%;background:var(--orange)}
.brand-name{font-family:"Ubuntu",sans-serif;font-weight:700;font-size:30px;color:var(--brand-blue-dark)}
.social{top:10px;right:132px;display:flex;gap:10px}
.social span{width:44px;height:44px;background:var(--orange);display:block}
.main-nav{left:414px;top:84px;display:flex;font-family:"Ubuntu",sans-serif;font-size:15px}
.main-nav a{padding:0 15px;height:38px;line-height:38px;color:#333;text-decoration:none}
.main-nav a.active{background:var(--brand-blue);color:var(--white)}

/* hero */
.hero{top:122px;height:520px}
.hero-photo{left:0;top:0;width:1200px;height:520px;background:linear-gradient(100deg,#8794a4 0%,#b9c2cc 40%,#d9dfe6 70%,#eef1f4 100%)}
.hero-copy{right:130px;top:68px;text-align:right;font-family:"Ubuntu",sans-serif;color:var(--brand-blue-dark)}
.hero-copy h1{font-weight:300;font-size:42px;line-height:64px}
.hero-copy h1 b{font-weight:500;font-size:54px}
.btn{display:inline-flex;align-items:center;justify-content:center;gap:12px;font-family:"Open Sans",sans-serif;font-size:16px;color:var(--white);border-radius:4px;text-decoration:none}
.btn-blue{background:linear-gradient(#2f6fb8,var(--brand-blue-dark));width:280px;height:62px}
.btn-orange{background:linear-gradient(#f0863a,#d9621a);width:187px;height:63px}
.btn-grey{background:linear-gradient(#8a8a8a,#606060);width:189px;height:60px}
.hero .btn{margin-top:22px}
.hero-tag{margin-top:38px;font-size:25px;line-height:34px;color:#222;letter-spacing:1px;font-weight:400}

/* leader */
.leader{top:642px;height:428px;background:linear-gradient(var(--navy),var(--navy-deep));color:var(--white)}
.leader h2{left:132px;top:38px;font-family:"Ubuntu",sans-serif;font-weight:300;font-size:40px}
.leader h2 b{font-weight:400;font-size:58px}
.leader .sub{left:134px;top:112px;font-family:"Ubuntu",sans-serif;font-size:28px}
.arrow-list{list-style:none}
.arrow-list li::before{content:"→";margin-right:6px;font-size:.8em;opacity:.8}
.leader .arrow-list{font-family:"Ubuntu",sans-serif;font-size:23px;line-height:43px}
.leader .after{left:134px;top:372px;font-size:19px}
.leader-photo{left:660px;top:26px;width:400px;height:370px;background:radial-gradient(ellipse at 50% 40%,#3b6bb0,#1e3f6e 70%,transparent 72%)}

/* partner */
.partner{top:1070px;height:427px;background:linear-gradient(#eeeeee,var(--grey-mid))}
.partner h2{left:128px;top:40px;font-family:"Ubuntu",sans-serif;font-weight:400;font-size:39px;color:var(--orange)}
.partner .arrow-list{font-size:19px;line-height:30px;color:var(--brand-blue)}
.partner .anywhere{left:220px;top:250px;font-size:22px;letter-spacing:1px;color:var(--orange)}
.partner .free{left:134px;top:308px;font-size:20px;line-height:28px;color:var(--brand-blue)}
.partner-photo{left:811px;top:74px;width:257px;height:250px;border-top:5px solid var(--orange);background:linear-gradient(135deg,#c9d8e8,#f3f6f9 55%,#7f8a96)}
.partner .btn{position:absolute;left:846px;top:295px}

/* audience */
.audience{top:1497px;height:559px;background:linear-gradient(var(--orange-soft),var(--orange))}
.audience h2{width:100%;text-align:center;top:46px;font-family:"Ubuntu",sans-serif;font-weight:400;font-size:42px;color:#3d3d3d}
.card{top:117px;width:298px;height:393px;background:var(--peach);border-radius:6px;box-shadow:0 2px 6px rgba(0,0,0,.2);text-align:center}
.card-photo{position:absolute;left:28px;top:0;width:242px;height:177px;background:linear-gradient(#d7dde4,#7c8794)}
.card h3{margin-top:190px;font-family:"Ubuntu",sans-serif;font-weight:400;font-size:21px;line-height:24px;color:#333}
.card p{margin:14px 22px 0;font-size:13px;line-height:19px;color:#444}

/* potential */
.potential{top:2056px;height:438px;background:var(--sun)}
.potential h2{width:100%;text-align:center;top:40px;font-family:"Ubuntu",sans-serif;font-weight:400;font-size:43px;color:var(--brand-blue)}
.potential-photo{left:137px;top:85px;width:413px;height:324px;background:radial-gradient(ellipse at 50% 50%,#6b8fc4,#f0c47a 70%)}
.mastered{left:530px;top:118px;font-family:"Ubuntu",sans-serif;font-size:23px;color:#444;display:flex;align-items:center;gap:10px}
.potential .arrow-list{left:590px;top:168px;font-size:19px;line-height:30px;color:#555}
.potential .btn{position:absolute;left:581px;top:264px}
.potential .journey{left:782px;top:268px;font-size:19px;line-height:30px;letter-spacing:2px;color:#666}
.potential .journey b{color:#555}
.potential .best{left:583px;top:356px;font-size:21px;color:#555}
.potential .best b{font-weight:700}

/* cta */
.cta{top:2494px;height:236px;background:var(--grey-light);text-align:center}
.cta h2{width:100%;top:44px;font-family:"Ubuntu",sans-serif;font-weight:400;font-size:39px;color:#3b3b3b}
.cta .btn{position:absolute;left:460px;top:122px}

/* footer */
.site-footer{top:2730px;height:216px;background:var(--footer);color:#ddd;font-size:14px}
.foot-links{width:100%;text-align:center}
.foot-links span{margin:0 10px;color:#888}
.copy{left:133px;top:148px;font-size:14px}
.connect{right:132px;top:158px;display:flex;align-items:center;gap:8px;font-size:14px}
.connect i{width:32px;height:32px;border-radius:50%;background:#eee;display:block}
</style>
</head>
<body>

<header class="site-header">
  <div class="brand abs"><span class="brand-mark"></span><span class="brand-name">Brightwell Careers</span></div>
  <div class="social abs" aria-label="Social links"><span></span><span></span><span></span></div>
  <nav class="main-nav abs">
    <a class="active" href="#">Transforming Leadership</a><a href="#">Assessments</a><a href="#">Coaching</a><a href="#">Resources &amp; Tools</a><a href="#">Bookings &amp; Prices</a>
  </nav>
</header>

<section class="hero">
  <div class="hero-photo ph" role="img" aria-label="Smiling businesswoman in front of a team meeting"></div>
  <div class="hero-copy abs">
    <h1>Want to <b>Motivate</b> your team to<br>Higher Performance Levels?</h1>
    <a class="btn btn-blue" href="#">
      <svg width="26" height="18" viewBox="0 0 26 18"><path d="M1 9 L7 3 L13 6 L19 3 L25 9 L15 16 Z" fill="#fff"/></svg>Schedule A Meeting Now</a>
    <p class="hero-tag">BRIGHTWELL CAREERS<br>VIRTUAL LEADERSHIP<br>COACHING &amp; ASSESSMENT</p>
  </div>
</section>

<section class="leader">
  <h2 class="abs">You are the <b>Leader</b></h2>
  <p class="sub abs">Your people expect you to:</p>
  <ul class="arrow-list abs" style="left:134px;top:156px">
    <li>Engage them</li><li>Inspire them</li><li>Motivate them</li><li>Develop them</li><li>Set vision</li>
  </ul>
  <ul class="arrow-list abs" style="left:344px;top:156px">
    <li>Define values</li><li>Create culture</li><li>Resolve conflicts</li><li>Solve problems</li><li>Choose winning strategies</li>
  </ul>
  <p class="after abs">...and take care of business as usual.</p>
  <div class="leader-photo ph" role="img" aria-label="Businessman with hands pressed together"></div>
  <span class="chev" style="bottom:-18px;border-top-color:var(--navy-deep)"></span>
</section>

<section class="partner">
  <h2 class="abs">Partner With Your Coach To:</h2>
  <ul class="arrow-list abs" style="left:134px;top:108px">
    <li>Define your goals</li><li>Assess your strengths</li><li>Define your development plan</li><li>Explore new perspectives</li>
  </ul>
  <ul class="arrow-list abs" style="left:434px;top:108px">
    <li>Practice winning strategies</li><li>Embed effective behaviours</li><li>Review performance improvement</li><li>Celebrate wins!</li>
  </ul>
  <p class="anywhere abs">ONLINE &nbsp;|&nbsp; ANYTIME &nbsp;|&nbsp; ANYWHERE</p>
  <p class="free abs">FREE PulseQ 3.0 Emotional Intelligence Leadership Assessment<br>for all Brightwell Careers Coaching Clients</p>
  <div class="partner-photo ph" role="img" aria-label="Two businesspeople shaking hands"></div>
  <a class="btn btn-orange" href="#">
    <svg width="20" height="24" viewBox="0 0 20 24"><path d="M7 2 v12 l-3-3 -2 2 6 9 h9 l2-9 v-4 h-8 V2 Z" fill="#fff"/></svg>Book Now</a>
  <span class="chev" style="bottom:-18px;border-top-color:var(--grey-mid)"></span>
</section>

<section class="audience">
  <h2 class="abs">Who is Leadership Assessment And Coaching For?</h2>
  <article class="card abs" style="left:132px">
    <div class="card-photo" role="img" aria-label="Group of organisational leaders"></div>
    <h3>Organisational<br>Leaders</h3>
    <p>"I really appreciate the great work Owen did with me to get my focus back on leading the business through a difficult change process. It definitely would have been much harder for me without the easy access to such a supportive sounding board. I'm now ready for the next big challenge."</p>
  </article>
  <article class="card abs" style="left:451px">
    <div class="card-photo" role="img" aria-label="HR managers standing together"></div>
    <h3>HR &amp; OD Managers<br>Learning Officers</h3>
    <p>"Online delivery is perfect for us. Managing a coordinated coaching program for a geographically dispersed leadership team is a real challenge. Using Brightwell Careers to organise the 360's and then the follow-up coaching, made life so much easier, both my Team and our internal clients"</p>
  </article>
  <article class="card abs" style="left:768px">
    <div class="card-photo" role="img" aria-label="Team leader in front of his team"></div>
    <h3>Team<br>Leaders</h3>
    <p>"I have learnt so much more, about myself and how to really connect with my team through this leadership coaching, than I ever have done in the many training programs I have attended. I talk things through with my coach whenever the need or a good moment comes up."</p>
  </article>
  <span class="chev" style="bottom:-18px;border-top-color:var(--orange)"></span>
</section>

<section class="potential">
  <h2 class="abs">Unlock You're Limitless Potential</h2>
  <div class="potential-photo ph" role="img" aria-label="Coach gesturing while speaking"></div>
  <p class="mastered abs">
    <svg width="40" height="36" viewBox="0 0 40 36"><rect x="2" y="2" width="36" height="24" fill="none" stroke="#555" stroke-width="3"/><rect x="10" y="14" width="4" height="8" fill="#555"/><rect x="18" y="9" width="4" height="13" fill="#555"/><rect x="26" y="12" width="4" height="10" fill="#555"/><path d="M20 26 v8 M12 34 h16" stroke="#555" stroke-width="3"/></svg>
    World Class Leaders have mastered:</p>
  <ul class="arrow-list abs">
    <li>Emotional Leadership</li><li>Tansormational Ledership</li><li>Values Based Leadership</li>
  </ul>
  <a class="btn btn-grey" href="#">
    <svg width="20" height="24" viewBox="0 0 20 24"><path d="M7 2 v12 l-3-3 -2 2 6 9 h9 l2-9 v-4 h-8 V2 Z" fill="#fff"/></svg>Book Now</a>
  <p class="journey abs">To start your <b>Leadership<br>Development</b> journey</p>
  <p class="best abs"><b>BE THE BEST</b> YOU CAN BE!</p>
  <span class="chev" style="bottom:-18px;border-top-color:var(--sun)"></span>
</section>

<section class="cta">
  <h2 class="abs">Want To Know How Brightwell Careers Can Help?</h2>
  <a class="btn btn-blue" href="#">
    <svg width="26" height="18" viewBox="0 0 26 18"><path d="M1 9 L7 3 L13 6 L19 3 L25 9 L15 16 Z" fill="#fff"/></svg>Schedule A Meeting Now</a>
</section>

<footer class="site-footer">
  <p class="foot-links abs" style="top:20px">Home<span>|</span>Transforming Leadership<span>|</span>Assessments<span>|</span>Coaching<span>|</span>Resources &amp; Tools<span>|</span>Bookings &amp; Prices</p>
  <p class="foot-links abs" style="top:82px">About<span>|</span>Contact<span>|</span>Terms &amp; Conditions<span>|</span>Privacy Policy</p>
  <p class="copy abs">Brightwell Careers. All Rights Reserved</p>
  <div class="connect abs">Connect with us: <i></i><i></i><i></i></div>
</footer>

</body>
</html>
```